Supplement label for Brain health

I need a design for a supplement this supplement is a brain boost supplement.

The Name is Cortiva Plus.

I have attached other labels I like. This is for 50 plus demographic so the lettering needs to be easy to read and stand out. I have attached a dummy label template that once the winner is choosen then they will get the real supplement facts etc.

Clean desgin easy to read.

This file must be finished in AI format.

Target Market(s)

50 plus 70 percent female 30 percent male

Industry/Entity Type

Supplement

Font styles to use
Other font styles liked:
• Myrid pro maybe

Requirements
Must have
• easy to read text so no colors that hide text or hard to read.

```html
<!DOCTYPE html>
<html lang="en">
<head>
<meta charset="utf-8">
<title>Cortiva Plus – Supplement Label</title>
<link href="https://fonts.googleapis.com/css2?family=PT+Sans:wght@400;700&family=Oswald:wght@500;600&family=Archivo+Black&display=swap" rel="stylesheet">
<style>
  :root{
    --bg:#d9d7d4;
    --label:#f4f5f6;
    --label-edge:#dfe2e5;
    --ink:#1d1d1f;
    --brand-blue:#1c5aa6;
    --navy:#0d2f6b;
    --facts-blue:#123c86;
    --teal:#2bb6d6;
    --sky:#3d8fd8;
    --orange:#f29a1f;
    --amber:#f7b52b;
    --yellow:#ffd21f;
    --red:#e03a1e;
    --white:#ffffff;
  }
  *{box-sizing:border-box;margin:0;padding:0}
  html,body{width:1200px;height:825px;overflow:hidden}
  body{background:var(--bg);font-family:"PT Sans",Arial,sans-serif;color:var(--ink);position:relative}

  .label{position:absolute;left:30px;top:195px;width:1140px;height:435px;background:var(--label);
    border:1px solid var(--label-edge);display:flex}
  .panel{position:relative;width:380px;height:100%}
  .panel + .panel{border-left:1px dashed var(--label-edge)}

  /* left panel */
  .usage{position:absolute;left:28px;top:34px;width:325px;font-size:11px;line-height:1.25}
  .usage b{font-weight:700}
  .caution{position:absolute;left:28px;top:82px;width:330px;height:175px;border-radius:14px;
    background:linear-gradient(135deg,var(--teal),var(--sky));color:var(--white);
    padding:14px 16px;font-size:10.5px;line-height:1.32;border:3px solid #e6eef3}
  .caution .caution-title{color:var(--yellow);font-weight:700}
  .disclaimer{position:absolute;left:28px;top:276px;width:250px;padding:6px 9px;border-radius:6px;
    background:var(--yellow);border:2px solid var(--sky);font-size:7.5px;line-height:1.3;font-weight:700}
  .distributor{position:absolute;left:32px;top:336px;font-family:"Oswald",sans-serif;font-weight:500;
    font-size:13px;line-height:1.3}

  /* centre panel */
  .brand{position:absolute;left:0;right:0;top:26px;text-align:center;font-family:"PT Sans",sans-serif;
    font-weight:700;font-size:46px;color:var(--brand-blue);letter-spacing:.5px}
  .brand-rule{position:absolute;left:50px;right:50px;top:86px;height:2px;background:var(--orange)}
  .illustration{position:absolute;left:75px;top:100px;width:230px;height:230px;border-radius:50%;
    background:radial-gradient(circle at 50% 50%,#2f6fc9 0%,#163f8f 45%,#0b2150 62%,#dfe8ee 64%,var(--label) 100%)}
  .badge{position:absolute;left:82px;top:345px;width:216px;height:38px;border-radius:19px;
    background:linear-gradient(var(--amber),var(--orange));border:2px solid var(--navy);
    font-family:"Oswald",sans-serif;font-weight:600;font-size:20px;color:var(--ink);
    display:flex;align-items:center;justify-content:center;letter-spacing:.5px}
  .count{position:absolute;width:46px;height:56px;background:var(--orange);border:2px solid var(--red);
    color:var(--red);font-family:"Oswald",sans-serif;text-align:center;line-height:1}
  .count .num{display:block;font-size:32px;font-weight:600;margin-top:3px}
  .count .unit{display:block;font-size:8px;font-weight:600;margin-top:2px}
  .count-centre{left:318px;top:290px}

  /* right panel */
  .facts{position:absolute;left:58px;top:30px;width:300px;background:var(--facts-blue);color:var(--white);
    border:2px solid var(--amber);padding:6px 8px 5px}
  .facts-title{font-family:"Archivo Black",sans-serif;color:var(--yellow);font-size:21px;line-height:1.1}
  .facts-serving{font-size:10px;line-height:1.2;padding-bottom:4px;border-bottom:3px solid var(--amber)}
  .facts-head{font-size:8px;padding:3px 0 2px;border-bottom:1px solid var(--amber)}
  .facts-row{display:flex;justify-content:space-between;font-size:9.5px;line-height:1.15;
    padding:1.5px 0;border-bottom:1px solid rgba(255,255,255,.35)}
  .facts-row .amt{padding-right:12px;white-space:nowrap}
  .facts-row em{font-style:italic}
  .facts-foot{font-size:9px;padding-top:2px;border-top:2px solid var(--amber)}
  .other{position:absolute;left:58px;top:288px;width:300px;font-size:9.5px;line-height:1.2}
  .other b{font-weight:700}
  .count-right{left:28px;top:330px}
  .warning{position:absolute;left:92px;top:335px;width:266px;background:var(--facts-blue);color:var(--white);
    font-size:9px;font-weight:700;line-height:1.25;padding:6px 8px;text-transform:uppercase}
</style>
</head>
<body>
  <section class="label">
    <div class="panel panel-left">
      <p class="usage"><b>SUGGESTED USE:</b> 1 capsule taken 1 to 2 times daily preferably with meals or as directed by a healthcare professional.</p>
      <div class="caution"><span class="caution-title">CAUTION:</span> Consult your healthcare provider before use if you are pregnant, nursing, taking medication, or have a medical condition. Discontinue use and consult a physician if any adverse reaction occurs. Do not exceed recommended dose. Not intended for use by persons under the age of 18. Keep container tightly closed after each use and protect from heat and moisture.</div>
      <p class="disclaimer">* These statements have not been evaluated by the Food &amp; Drug Administration. This product is not intended to diagnose, treat, cure or prevent any disease.</p>
      <p class="distributor">Distributed by:<br>Company Name<br>Full Address and Phone</p>
    </div>

    <div class="panel panel-centre">
      <h1 class="brand">Cortiva Plus</h1>
      <div class="brand-rule"></div>
      <div class="illustration" role="img" aria-label="Blue circuit-board brain illustration framed by coloured arcs"></div>
      <div class="badge">DIETARY SUPPLEMENT</div>
      <div class="count count-centre"><span class="num">30</span><span class="unit">CAPSULES</span></div>
    </div>

    <div class="panel panel-right">
      <div class="facts">
        <div class="facts-title">Supplement Facts</div>
        <div class="facts-serving">Serving Size 1 Capsule<br>Servings Per Container: 30</div>
        <div class="facts-head">Amt Per Serv. &nbsp; %DV/RDI</div>
        <div class="facts-row"><span><em>Ginkgo biloba</em> Leaf (24% extract)</span><span class="amt">50mg *</span></div>
        <div class="facts-row"><span>Phosphatidylserine 4% Complex<br>(consisting of Lecithin and Phosphatidylserine)</span><span class="amt">125mg *</span></div>
        <div class="facts-row"><span>N-Acetyl L-Carnitine HCl</span><span class="amt">50mg *</span></div>
        <div class="facts-row"><span>St. John's Wort (0.3% extract)<br>(flower heads)</span><span class="amt">250mg *</span></div>
        <div class="facts-row"><span>L-Glutamine</span><span class="amt">150mg *</span></div>
        <div class="facts-row"><span><em>Bacopa monnieri</em> Leaf Extract<br>(20% bacosides)</span><span class="amt">120mg *</span></div>
        <div class="facts-row"><span>Vinpocetine (seeds)</span><span class="amt">2mg *</span></div>
        <div class="facts-row"><span>Huperzine-A (aerial plant)</span><span class="amt">10mcg *</span></div>
        <div class="facts-foot">*Daily Value not established.</div>
      </div>
      <p class="other"><b>Other ingredients:</b> Gelatin (bovine), microcrystalline cellulose, vegetable magnesium stearate, and silicon dioxide.<br><b>ALLERGEN WARNING: CONTAINS SOY (LECITHIN).</b></p>
      <div class="count count-right"><span class="num">30</span><span class="unit">CAPSULES</span></div>
      <p class="warning">Keep out of the reach of children.<br>Do not use if safety seal is damaged or missing. Store in a cool, dry place.</p>
    </div>
  </section>
</body>
</html>
```